Zerbani Facilities Management brochure

to design suitable company brochure compatible with company scope work, ee are at Zerbani handling all soft services such as housekeeping , landscaping, waste mangement and pest control and hard services such as building renovations and MEP maintenance ,,,,,,,,,,,,................nnnñnnnnnnnnnnnnnnnnnnnnnnnnnnnnnnnnnnnnnnmnñmmmmmmmmmmmmmmmmm

Target Market(s)

Saudi Arabia

Industry/Entity Type

Facilities Management

Font styles to use
Serif

Requirements
Must have
• Thems matching facilities management feild
Nice to have
• Innovation
Should not have
• Strangers faces photos

```html
<!DOCTYPE html>
<html lang="en">
<head>
<meta charset="utf-8">
<title>Zerbani Facilities Management brochure</title>
<link rel="stylesheet" href="https://fonts.googleapis.com/css2?family=Montserrat:wght@400;500;600;700;800&display=swap">
<style>
:root{
  --navy:#1d3a6e;
  --navy-deep:#172f5b;
  --orange:#ef7d22;
  --gold:#f2a71b;
  --red:#a53138;
  --white:#ffffff;
  --ink:#3a3f4a;
  --sans:'Montserrat', Arial, sans-serif;
}
*{box-sizing:border-box;margin:0;padding:0}
html,body{width:1200px;height:4353px;overflow:hidden;background:var(--white);font-family:var(--sans)}
.canvas{position:relative;width:1200px;height:4353px}
.band{position:absolute;left:0;width:1200px;overflow:hidden}
.band-cover{top:0;height:795px;background:linear-gradient(180deg,#e2d6ce,#d9cbc2)}
.band-inner{top:795px;height:825px;background:#c9bbb2}
.band-outer{top:1620px;height:825px;background:linear-gradient(180deg,#d7cac1,#ece2da)}

.spread{position:relative;width:936px;height:724px;background:var(--navy);color:var(--white);overflow:hidden}
.spread>svg{position:absolute;left:0;top:0;width:936px;height:724px}
.abs{position:absolute}

.stage{position:absolute;left:202px;top:104px;transform:scale(.85);transform-origin:0 0;box-shadow:0 18px 40px rgba(40,30,25,.28)}
.cover-crop{position:absolute;left:366px;top:42px;width:468px;height:724px;overflow:hidden;transform:scale(.98);transform-origin:0 0;box-shadow:0 18px 40px rgba(40,30,25,.28)}
.cover-crop .spread{position:absolute;left:-468px;top:0}
.canvas>.spread.flat-outer{position:absolute;left:132px;top:2611px;box-shadow:0 4px 14px rgba(0,0,0,.22)}
.canvas>.spread.flat-inner{position:absolute;left:132px;top:3468px;box-shadow:0 4px 14px rgba(0,0,0,.22)}

.brand-name{font-family:var(--sans);font-weight:600;font-size:24px;color:var(--navy);display:flex;align-items:center;gap:8px}
.brand-name .mark{width:22px;height:22px;background:var(--orange)}
.brand-name.light{color:var(--white);font-size:17px}
.brand-name.light .mark{width:16px;height:16px}

.contact-title{left:36px;top:238px;font-size:21px;font-weight:500;letter-spacing:.5px}
.contact-title b{font-weight:700}
.label{color:var(--gold);font-weight:600;font-size:12.5px}
.address-label{left:36px;top:300px}
.address{left:36px;top:336px;font-size:10.5px;line-height:1.28}
.contact-row{left:36px;top:440px;display:flex;font-size:10.5px}
.contact-row .cell{padding:0 16px;border-left:1.5px solid rgba(255,255,255,.8)}
.contact-row .cell:first-child{padding-left:0;border-left:none}
.contact-row .label{display:block;margin-bottom:6px}

.headline{left:505px;top:455px;font-weight:800;font-size:39px;line-height:1.1;letter-spacing:.3px}
.headline .accent{color:var(--gold)}
.site{font-weight:500;font-size:13px;letter-spacing:1.4px}
.site.cover{left:505px;top:662px}

.body-copy{left:36px;top:38px;width:405px;font-size:9.4px;line-height:1.3}
.body-copy p{margin-bottom:11px}
.md-title{left:36px;top:580px;font-size:21px;font-weight:500;color:var(--navy-deep);white-space:nowrap}
.md-copy{left:36px;top:616px;width:400px;font-size:9.4px;line-height:1.3;color:var(--ink)}
.page-no{left:438px;top:655px;font-size:30px;color:var(--gold);font-weight:500}
.leader-title{left:546px;top:66px;font-size:21px;font-weight:500}
.leader-title b{color:var(--gold);font-weight:700}
.leader-copy{left:546px;top:104px;width:326px;font-size:9.4px;line-height:1.3}
.quote{font-size:44px;font-weight:800;color:var(--gold);line-height:1}
.site.inner{left:730px;top:680px;color:var(--white)}
</style>
</head>
<body>
<svg width="0" height="0" style="position:absolute" aria-hidden="true">
  <defs>
    <linearGradient id="skyPhoto" x1="0" y1="0" x2="0" y2="1">
      <stop offset="0" stop-color="#5b93d4"/>
      <stop offset=".45" stop-color="#b9d3ee"/>
      <stop offset=".75" stop-color="#3f78bf"/>
      <stop offset="1" stop-color="#25508f"/>
    </linearGradient>
    <linearGradient id="towerPhoto" x1="0" y1="0" x2="1" y2="0">
      <stop offset="0" stop-color="#7b3b5e"/>
      <stop offset="1" stop-color="#5a2f58"/>
    </linearGradient>
    <linearGradient id="lowerPhoto" x1="0" y1="0" x2="1" y2="1">
      <stop offset="0" stop-color="#b9404a"/>
      <stop offset=".55" stop-color="#5a79a8"/>
      <stop offset="1" stop-color="#c9d4e2"/>
    </linearGradient>
    <radialGradient id="portrait" cx=".5" cy=".45" r=".6">
      <stop offset="0" stop-color="#e9e4dc"/>
      <stop offset="1" stop-color="#8c6d4d"/>
    </radialGradient>
    <linearGradient id="scene" x1="0" y1="0" x2="0" y2="1">
      <stop offset="0" stop-color="#24427a"/>
      <stop offset=".55" stop-color="#e5962e"/>
      <stop offset="1" stop-color="#2a4a84"/>
    </linearGradient>
  </defs>
</svg>

<main class="canvas">

  <section class="band band-cover">
    <div class="cover-crop">
      <div class="spread outer-spread">
        <svg viewBox="0 0 936 724" aria-hidden="true">
          <rect width="936" height="724" fill="var(--navy)"/>
          <g role="img" aria-label="Photograph of the company headquarters building against a blue sky">
            <path d="M0,0H936V385C860,382 700,378 620,350C520,315 440,170 330,130C220,95 90,112 0,124Z" fill="url(#skyPhoto)"/>
            <path d="M760,40L880,0V395L760,385Z" fill="url(#towerPhoto)"/>
          </g>
          <path d="M0,124C90,112 220,95 330,130C440,170 520,315 620,350C700,378 860,382 936,385" fill="none" stroke="var(--orange)" stroke-width="5"/>
          <path d="M0,505L270,540V716H0Z" fill="url(#lowerPhoto)" role="img" aria-label="Photograph of a company building"/>
          <rect x="0" y="716" width="936" height="8" fill="var(--orange)"/>
          <rect x="318" y="525" width="112" height="62" rx="8" fill="rgba(255,255,255,.85)"/>
          <rect x="760" y="598" width="112" height="62" rx="8" fill="rgba(255,255,255,.85)"/>
        </svg>
        <div class="abs brand-name" style="left:510px;top:78px">Zerbani<span class="mark"></span></div>
        <h2 class="abs contact-title">CONTACT <b>US</b></h2>
        <div class="abs label address-label">Address &amp; Office :</div>
        <p class="abs address">Zerbani Sons Company (L.L.C),<br>Al Noor Street,<br>Al Noor Street Al Rawdah,<br>Dammam,<br>Eastern Province,<br>Kingdom of Saudi Arabia</p>
        <div class="abs contact-row">
          <div class="cell"><span class="label">Phone :</span>966 3 5550142</div>
          <div class="cell"><span class="label">Email:</span>info@zerbani-fm.com</div>
          <div class="cell"><span class="label">Website :</span>www.zerbani-fm.com</div>
        </div>
        <div class="abs brand-name light" style="left:318px;top:640px">Zerbani<span class="mark"></span></div>
        <h1 class="abs headline">YOUR SUCCESS<br>IS OUR PRIMARY<br><span class="accent">GOAL</span></h1>
        <div class="abs site cover">www.zerbani-fm.com</div>
      </div>
    </div>
  </section>

  <section class="band band-inner">
    <div class="stage">
      <div class="spread inner-spread">
        <svg viewBox="0 0 936 724" aria-hidden="true">
          <rect width="936" height="724" fill="var(--navy)"/>
          <path d="M0,470C120,440 250,520 340,532C400,540 440,530 468,522C560,500 640,560 700,724H0Z" fill="var(--white)"/>
          <circle cx="135" cy="470" r="74" fill="var(--white)"/>
          <circle cx="135" cy="470" r="69" fill="url(#portrait)" role="img" aria-label="Portrait photograph of the managing director"/>
          <line x1="36" y1="700" x2="440" y2="700" stroke="var(--gold)" stroke-width="1.5"/>
          <rect x="520" y="42" width="370" height="128" rx="16" fill="none" stroke="var(--gold)" stroke-width="2.5"/>
          <rect x="540" y="200" width="380" height="360" fill="url(#scene)" opacity=".85" role="img" aria-label="Illustration of a team steering a paper boat towards growth"/>
          <path d="M560,724C700,700 820,640 936,520V724Z" fill="var(--red)"/>
          <path d="M560,712C700,688 820,628 936,506" fill="none" stroke="var(--orange)" stroke-width="3"/>
          <line x1="468" y1="0" x2="468" y2="724" stroke="rgba(0,0,0,.12)"/>
        </svg>
        <div class="abs body-copy">
          <p>Today, change is everywhere. Our customers' markets are moving quickly in response to new technology, stricter standards and rising service expectations. Sustainability is often the driver of demand for better, cleaner and more efficient buildings. For companies that see potential in these challenges, this is a good time to be in business. Since our foundation, Zerbani has adapted quickly to customer needs and market requirements, and our tradition of ingenuity drives continuous improvement in the way we operate.</p>
          <p>Today, Zerbani &amp; Sons Company is transforming itself to take advantage of the latest wave of change. We are reshaping our business units to meet new demands in growing markets, including facilities management, technical services, landscaping and waste care. This transformation aims at making us more agile and cost efficient.</p>
          <p>A growing world needs cost effective, efficient services, while meeting rigid safety standards. It needs an innovative and skilled workforce whom we continuously train to face new challenges. Here, you will also discover our commitment to the communities where we live and work, and how we protect the environment we all share.</p>
          <p>At Zerbani &amp; Sons Company, we have always found excitement in challenge. As you browse through these pages, you will get a sense of the passion, expertise and reliability we bring to every site we serve.</p>
        </div>
        <h2 class="abs md-title">Message From Managing Director</h2>
        <p class="abs md-copy">It gives me great pleasure to welcome you to Zerbani &amp; Sons Company. Here you will find a full review of our company, reflecting the pride of our employees who contribute to our ongoing growth and success. It also conveys our sense of mission and vision to become the preferred partner in facilities support services.</p>
        <div class="abs page-no">1</div>
        <div class="abs quote" style="left:528px;top:30px">“</div>
        <h2 class="abs leader-title">Our <b>Leadership</b> Team</h2>
        <p class="abs leader-copy">We strongly believe in long-term partnerships with a clear roadmap on benefits to our clients on cost, process, infrastructure upgrades and efficiency gains. Our client retention since inception is a strong testimony of our service excellence and cost effectiveness.</p>
        <div class="abs quote" style="left:838px;top:150px">”</div>
        <div class="abs site inner">www.zerbani-fm.com</div>
      </div>
    </div>
  </section>

  <section class="band band-outer">
    <div class="stage">
      <div class="spread outer-spread">
        <svg viewBox="0 0 936 724" aria-hidden="true">
          <rect width="936" height="724" fill="var(--navy)"/>
          <g role="img" aria-label="Photograph of the company headquarters building against a blue sky">
            <path d="M0,0H936V385C860,382 700,378 620,350C520,315 440,170 330,130C220,95 90,112 0,124Z" fill="url(#skyPhoto)"/>
            <path d="M760,40L880,0V395L760,385Z" fill="url(#towerPhoto)"/>
          </g>
          <path d="M0,124C90,112 220,95 330,130C440,170 520,315 620,350C700,378 860,382 936,385" fill="none" stroke="var(--orange)" stroke-width="5"/>
          <path d="M0,505L270,540V716H0Z" fill="url(#lowerPhoto)" role="img" aria-label="Photograph of a company building"/>
          <rect x="0" y="716" width="936" height="8" fill="var(--orange)"/>
          <rect x="318" y="525" width="112" height="62" rx="8" fill="rgba(255,255,255,.85)"/>
          <rect x="760" y="598" width="112" height="62" rx="8" fill="rgba(255,255,255,.85)"/>
          <line x1="468" y1="0" x2="468" y2="724" stroke="rgba(0,0,0,.12)"/>
        </svg>
        <div class="abs brand-name" style="left:510px;top:78px">Zerbani<span class="mark"></span></div>
        <h2 class="abs contact-title">CONTACT <b>US</b></h2>
        <div class="abs label address-label">Address &amp; Office :</div>
        <p class="abs address">Zerbani Sons Company (L.L.C),<br>Al Noor Street,<br>Al Noor Street Al Rawdah,<br>Dammam,<br>Eastern Province,<br>Kingdom of Saudi Arabia</p>
        <div class="abs contact-row">
          <div class="cell"><span class="label">Phone :</span>966 3 5550142</div>
          <div class="cell"><span class="label">Email:</span>info@zerbani-fm.com</div>
          <div class="cell"><span class="label">Website :</span>www.zerbani-fm.com</div>
        </div>
        <div class="abs brand-name light" style="left:318px;top:640px">Zerbani<span class="mark"></span></div>
        <h1 class="abs headline">YOUR SUCCESS<br>IS OUR PRIMARY<br><span class="accent">GOAL</span></h1>
        <div class="abs site cover">www.zerbani-fm.com</div>
      </div>
    </div>
  </section>

  <div class="spread outer-spread flat-outer">
    <svg viewBox="0 0 936 724" aria-hidden="true">
      <rect width="936" height="724" fill="var(--navy)"/>
      <g role="img" aria-label="Photograph of the company headquarters building against a blue sky">
        <path d="M0,0H936V385C860,382 700,378 620,350C520,315 440,170 330,130C220,95 90,112 0,124Z" fill="url(#skyPhoto)"/>
        <path d="M760,40L880,0V395L760,385Z" fill="url(#towerPhoto)"/>
      </g>
      <path d="M0,124C90,112 220,95 330,130C440,170 520,315 620,350C700,378 860,382 936,385" fill="none" stroke="var(--orange)" stroke-width="5"/>
      <path d="M0,505L270,540V716H0Z" fill="url(#lowerPhoto)" role="img" aria-label="Photograph of a company building"/>
      <rect x="0" y="716" width="936" height="8" fill="var(--orange)"/>
      <rect x="318" y="525" width="112" height="62" rx="8" fill="rgba(255,255,255,.85)"/>
      <rect x="760" y="598" width="112" height="62" rx="8" fill="rgba(255,255,255,.85)"/>
      <line x1="468" y1="0" x2="468" y2="724" stroke="rgba(0,0,0,.12)"/>
    </svg>
    <div class="abs brand-name" style="left:510px;top:78px">Zerbani<span class="mark"></span></div>
    <h2 class="abs contact-title">CONTACT <b>US</b></h2>
    <div class="abs label address-label">Address &amp; Office :</div>
    <p class="abs address">Zerbani Sons Company (L.L.C),<br>Al Noor Street,<br>Al Noor Street Al Rawdah,<br>Dammam,<br>Eastern Province,<br>Kingdom of Saudi Arabia</p>
    <div class="abs contact-row">
      <div class="cell"><span class="label">Phone :</span>966 3 5550142</div>
      <div class="cell"><span class="label">Email:</span>info@zerbani-fm.com</div>
      <div class="cell"><span class="label">Website :</span>www.zerbani-fm.com</div>
    </div>
    <div class="abs brand-name light" style="left:318px;top:640px">Zerbani<span class="mark"></span></div>
    <h1 class="abs headline">YOUR SUCCESS<br>IS OUR PRIMARY<br><span class="accent">GOAL</span></h1>
    <div class="abs site cover">www.zerbani-fm.com</div>
  </div>

  <div class="spread inner-spread flat-inner">
    <svg viewBox="0 0 936 724" aria-hidden="true">
      <rect width="936" height="724" fill="var(--navy)"/>
      <path d="M0,470C120,440 250,520 340,532C400,540 440,530 468,522C560,500 640,560 700,724H0Z" fill="var(--white)"/>
      <circle cx="135" cy="470" r="74" fill="var(--white)"/>
      <circle cx="135" cy="470" r="69" fill="url(#portrait)" role="img" aria-label="Portrait photograph of the managing director"/>
      <line x1="36" y1="700" x2="440" y2="700" stroke="var(--gold)" stroke-width="1.5"/>
      <rect x="520" y="42" width="370" height="128" rx="16" fill="none" stroke="var(--gold)" stroke-width="2.5"/>
      <rect x="540" y="200" width="380" height="360" fill="url(#scene)" opacity=".85" role="img" aria-label="Illustration of a team steering a paper boat towards growth"/>
      <path d="M560,724C700,700 820,640 936,520V724Z" fill="var(--red)"/>
      <path d="M560,712C700,688 820,628 936,506" fill="none" stroke="var(--orange)" stroke-width="3"/>
    </svg>
    <div class="abs body-copy">
      <p>Today, change is everywhere. Our customers' markets are moving quickly in response to new technology, stricter standards and rising service expectations. Sustainability is often the driver of demand for better, cleaner and more efficient buildings. For companies that see potential in these challenges, this is a good time to be in business. Since our foundation, Zerbani has adapted quickly to customer needs and market requirements, and our tradition of ingenuity drives continuous improvement in the way we operate.</p>
      <p>Today, Zerbani &amp; Sons Company is transforming itself to take advantage of the latest wave of change. We are reshaping our business units to meet new demands in growing markets, including facilities management, technical services, landscaping and waste care. This transformation aims at making us more agile and cost efficient.</p>
      <p>A growing world needs cost effective, efficient services, while meeting rigid safety standards. It needs an innovative and skilled workforce whom we continuously train to face new challenges. Here, you will also discover our commitment to the communities where we live and work, and how we protect the environment we all share.</p>
      <p>At Zerbani &amp; Sons Company, we have always found excitement in challenge. As you browse through these pages, you will get a sense of the passion, expertise and reliability we bring to every site we serve.</p>
    </div>
    <h2 class="abs md-title">Message From Managing Director</h2>
    <p class="abs md-copy">It gives me great pleasure to welcome you to Zerbani &amp; Sons Company. Here you will find a full review of our company, reflecting the pride of our employees who contribute to our ongoing growth and success. It also conveys our sense of mission and vision to become the preferred partner in facilities support services.</p>
    <div class="abs page-no">1</div>
    <div class="abs quote" style="left:528px;top:30px">“</div>
    <h2 class="abs leader-title">Our <b>Leadership</b> Team</h2>
    <p class="abs leader-copy">We strongly believe in long-term partnerships with a clear roadmap on benefits to our clients on cost, process, infrastructure upgrades and efficiency gains. Our client retention since inception is a strong testimony of our service excellence and cost effectiveness.</p>
    <div class="abs quote" style="left:838px;top:150px">”</div>
    <div class="abs site inner">www.zerbani-fm.com</div>
  </div>

</main>
</body>
</html>
```